Topics to Raise With a Clinician tri-fold brochure

We are looking for a 1 page (front and back) 8.5" x 11" tri-fold brochure. Please refer back to our Rack Cards for a similar look and feel to the design. They can be found here: https://otvenrix.org/resources/sunny-garden-steady-mind-rack-card-series/.
This brochure is titled: Topics to Raise With a Clinician on Forgetfulness.

The document is for older readers. Do not put text over graphics and keep it simple and easy to read with high contrast.

We want some very simple design element(s) incorporated that convey Native American communities or heritage. But NO headdress, teepee graphics, owls etc. I have included some images, please use your creative discretion to use which ones look good.

Please remember to include the funding statement - it can be in a very small font 6/7 point: For more information about our project, please visit https://otvenrix.org/mind-care/resources - This rack card is supported by the Bureau for Wellness Tracking and Outreach (BWTO) of the Federal Office of Wellbeing and Family Supports (FWF) as part of a financial assistance award totaling $1,053,119.36 with 100 percent funded by BWTO/FWF. The contents are those of the author(s) and do not necessarily represent the official views of, nor an endorsement, by BWTO/FWF, or the U.S. Government.

Please feel free to choose one of each of the 2 logos that looks best (horizontal or square). We have the OT3 logo and the Cedar Path Learning Hub logo we would like to add. I have added the document and there are images to choose from to use.

I am thinking that the front of the tri-fold should have one of the pictures of a patient and doctor talking. I have included several options. Please use your creative discretion to choose what looks best.

Please let me know if you have any questions, thank you!

```html
<!DOCTYPE html>
<html lang="en">
<head>
<meta charset="utf-8">
<title>Topics to Raise With a Clinician on Forgetfulness</title>
<link href="https://fonts.googleapis.com/css2?family=Didact+Gothic&family=Outfit:wght@700&display=swap" rel="stylesheet">
<style>
  :root {
    --sky: #b4c9e9;
    --cocoa: #5e3530;
    --teal: #3b6f73;
    --clay: #a65b52;
    --deep-teal: #24444b;
    --dot: #6b3a33;
    --ink: #1d1d1d;
    --cream: #ffffff;
  }
  * { box-sizing: border-box; margin: 0; padding: 0; }
  html, body { width: 1200px; height: 927px; overflow: hidden; background: #fff; }
  body { font-family: "Didact Gothic", "Century Gothic", sans-serif; color: var(--ink); }
  .spread { position: relative; width: 1200px; height: 927px; }
  .panel { position: absolute; top: 0; height: 927px; overflow: hidden; }
  .band { position: absolute; display: flex; }
  .band span { display: block; height: 100%; }

  /* Intro panel */
  .panel--intro { left: 0; width: 397px; background: var(--sky); }
  .intro-text { position: absolute; top: 42px; left: 18px; width: 361px; text-align: center; font-size: 17px; line-height: 21.8px; }
  .intro-text p + p { margin-top: 21.8px; }
  .intro-photo { position: absolute; left: 0; top: 470px; width: 397px; height: 431px;
    background: linear-gradient(180deg, rgba(180,201,233,0) 0%, #8fb07a 30%, #5f8a4a 60%, #4a6f9a 100%); }

  /* Questions panel */
  .panel--ask { left: 397px; width: 400px; background: var(--cocoa); color: var(--cream); }
  .ask-photo { position: absolute; left: 0; top: 0; width: 400px; height: 226px;
    background: linear-gradient(135deg, #b9b3ad 0%, #8c7f86 45%, #5a4d6e 100%); }
  .ask-body { position: absolute; left: 16px; top: 268px; width: 380px; }
  .ask-title { font-family: "Outfit", "Century Gothic", sans-serif; font-weight: 700; font-size: 22px; line-height: 28px; margin-bottom: 20px; }
  .ask-list { list-style: none; font-size: 17px; line-height: 22px; }
  .ask-list > li { position: relative; padding-left: 30px; margin-bottom: 21px; }
  .num { position: absolute; left: 0; top: -1px; width: 24px; height: 24px; border-radius: 50%;
    background: #6e9c9d; color: #fff; font-family: "Outfit", sans-serif; font-size: 16px; line-height: 24px; text-align: center; }
  .sub-list { list-style: none; margin-left: 13px; }
  .sub-list li { position: relative; padding-left: 13px; }
  .sub-list li::before { content: "•"; position: absolute; left: -2px; }
  .sub-list li.plain::before { content: none; }

  /* Clinician panel */
  .panel--clinician { left: 797px; width: 403px; background: linear-gradient(180deg, #ffffff 0%, #f4f4f4 60%, #e8e6e3 100%); }
  .clin-head { position: absolute; left: 23px; top: 34px; }
  .clin-title { font-family: "Outfit", "Century Gothic", sans-serif; font-weight: 700; font-size: 22px; line-height: 29px; color: #111; }
  .clin-sub { font-size: 18px; line-height: 28px; margin-top: 1px; }
  .clin-list { position: absolute; left: 23px; top: 151px; width: 375px; list-style: none; font-size: 17px; line-height: 27.3px; }
  .clin-list li { position: relative; padding-left: 20px; }
  .clin-list li::before { content: ""; position: absolute; left: 0; top: 8px; width: 14px; height: 14px; border-radius: 50%; background: var(--dot); }
  .clin-photo { position: absolute; left: 0; top: 577px; width: 403px; height: 350px;
    background: linear-gradient(180deg, rgba(240,240,238,0) 0%, #dcd8d2 30%, #c9bfb6 65%, #b7aaa0 100%); }
</style>
</head>
<body>
<div class="spread">

  <section class="panel panel--intro">
    <div class="band" style="top:0;left:0;width:397px;height:17px;"><span style="width:222px;background:var(--teal)"></span><span style="width:175px;background:var(--clay)"></span></div>
    <div class="intro-text">
      <p>In our communities, memory and wisdom are sacred. When our Elders begin to experience changes in how they remember, think, or act, it's important to understand what's happening, so we can care for them with knowledge, love,and respect.</p>
      <p>Memory loss can progress to dementia. Dementia is a group of conditions that affect memory, thinking, and the ability to carry out everyday tasks.<br>Alzheimer's disease is the most common typeof dementia, but there are other types, too.</p>
      <p>If you are concerned about or experiencing memory loss, it's important to talk<br>to your doctor.<br>The following pages can help you start the conversation.</p>
    </div>
    <div class="intro-photo" role="img" aria-label="Elder man playing a ukulele outdoors among palm trees"></div>
    <div class="band" style="bottom:0;left:0;width:397px;height:26px;"><span style="width:297px;background:var(--cocoa)"></span><span style="width:100px;background:var(--teal)"></span></div>
  </section>

  <section class="panel panel--ask">
    <div class="ask-photo" role="img" aria-label="Caregiver's hands resting on an elder woman's shoulders"></div>
    <div class="band" style="top:226px;left:0;width:400px;height:17px;"><span style="width:297px;background:var(--teal)"></span><span style="width:103px;background:var(--clay)"></span></div>
    <div class="ask-body">
      <h2 class="ask-title">Topics to Raise With a Clinician:</h2>
      <ol class="ask-list">
        <li><span class="num">1</span>When should I be concerned?</li>
        <li><span class="num">2</span>What kind of testing can be done for memory loss?</li>
        <li><span class="num">3</span>What other things could be causing memory loss?
          <ul class="sub-list">
            <li>Anxiety or depression</li>
            <li>Sleep disorders</li>
            <li>Thyroid problems</li>
            <li>Vitamin deficiencies</li>
            <li>Head injuries</li>
            <li>Dehydration</li>
            <li>Infections<br>(Urinary tract, Respiratory, etc.)</li>
            <li class="plain">Medications</li>
          </ul>
        </li>
        <li><span class="num">4</span>What happens after diagnosis?
          <ul class="sub-list">
            <li>Are there lifestyle changes that could help?</li>
            <li>What safety measures should be taken?</li>
            <li>What are the signs of certain activities becoming unsafe?</li>
            <li>What community resources are available?</li>
            <li>How can we prepare for progression?</li>
          </ul>
        </li>
      </ol>
    </div>
    <div class="band" style="bottom:0;left:0;width:400px;height:26px;"><span style="width:21px;background:var(--teal)"></span><span style="width:379px;background:var(--deep-teal)"></span></div>
  </section>

  <section class="panel panel--clinician">
    <div class="band" style="top:0;left:0;width:403px;height:14px;"><span style="width:297px;background:var(--deep-teal)"></span><span style="width:106px;background:var(--clay)"></span></div>
    <div class="clin-head">
      <h2 class="clin-title">Questions Your Doctor<br>May Ask You:</h2>
      <p class="clin-sub">Suggested by Dr. Marwell</p>
    </div>
    <ul class="clin-list">
      <li>When did your symptoms of forgetfulness begin?</li>
      <li>What tasks do you find difficult?</li>
      <li>What specific behaviors related to memory loss are concerning you?</li>
      <li>Have you recently been sick?</li>
      <li>Have you recently been in an accident?</li>
      <li>Have you recently fallen or hit your head?</li>
      <li>Have you recently had a loss of someone who is close to you?</li>
      <li>Have there been any recent major changes in your life?</li>
      <li>Have you been dealing with a stressful event in your life?</li>
    </ul>
    <div class="clin-photo" role="img" aria-label="Older patient handing a paper to a smiling clinician in an exam room"></div>
  </section>

</div>
</body>
</html>
```